Business Card Design

We need a business card design for a new company. We produce and sell fully grown topiary (please Google topiary pictures if you are not familiar with Topiary).We make many different topiary designs and shapes in all sizes. Ranging from cute little table top animal sculptures such as bunnies and swans for the indoors, to big sculptures such as actual size elephants for outdoor gardens and parks. We also make topiary balls, spiral shapes and other attractive geometrical shapes for indoor and outdoor decorations. We want to see designs that reflects the playfulness and ,liveliness and cute characteristics of our products.Please find attached the logo.Thank you

Industry/Entity Type

Business

Contact Information for Business Card

Company Name : Leaf Forge
Slogan : Shaping Every Garden Bright
Tagline: Topiary...and more
Website : www.leafforge.example

Name on Card : Youssef Nabil Darwish
Title : Founder & CEO
email: youssef_nabil@leafforge.example

Address : 27 El-Masry Street
Ground Floor,Ste.1
El-Marg,Cairo,Egypt

Office Telephone : (02) 25948017
Mobile Number : 01287719462

Requirements
Must have
• The business card must have a white background.

```html
<!DOCTYPE html>
<html lang="en">
<head>
<meta charset="utf-8">
<title>Leaf Forge – Business Card</title>
<link rel="stylesheet" href="https://fonts.googleapis.com/css2?family=Open+Sans:wght@400;700&family=Caveat:wght@400&display=swap">
<style>
  :root {
    --leaf: #5e9a2f;
    --leaf-dark: #4f8726;
    --ink: #111111;
    --paper: #ffffff;
    --backdrop: #e9ece6;
  }
  * { box-sizing: border-box; margin: 0; padding: 0; }
  html, body { width: 1200px; height: 846px; overflow: hidden; }
  body {
    background: var(--backdrop);
    font-family: "Open Sans", Arial, sans-serif;
    position: relative;
  }
  .card {
    position: absolute;
    left: 80px; top: 123px;
    width: 1040px; height: 600px;
    background: var(--paper);
    border-radius: 44px;
    overflow: hidden;
    box-shadow: 0 6px 24px rgba(0,0,0,.15);
  }
  .brand-name {
    position: absolute;
    left: 140px; top: 40px;
    font-size: 124px;
    font-weight: 400;
    color: var(--leaf);
    line-height: 1;
    letter-spacing: -1px;
  }
  .slogan {
    position: absolute;
    left: 250px; top: 196px;
    font-family: "Caveat", cursive;
    font-size: 50px;
    color: var(--leaf);
    transform: rotate(-4deg);
    transform-origin: left center;
  }
  .person {
    position: absolute;
    left: 52px; top: 382px;
    color: var(--leaf);
  }
  .person-name { font-size: 29px; font-weight: 700; text-transform: uppercase; letter-spacing: .3px; }
  .person-title { font-size: 29px; font-weight: 400; text-transform: uppercase; margin-top: 2px; }
  .contacts {
    position: absolute;
    left: 470px; top: 282px;
    list-style: none;
    color: var(--ink);
    font-size: 23px;
    font-weight: 700;
  }
  .contacts li { display: flex; align-items: flex-start; gap: 14px; margin-bottom: 12px; line-height: 1.25; }
  .contacts svg { width: 26px; height: 26px; flex: none; margin-top: 2px; }
  .band { position: absolute; left: 0; top: 0; width: 1040px; height: 600px; }
  .website {
    position: absolute;
    left: 300px; top: 522px;
    color: var(--paper);
    font-size: 31px;
    font-weight: 700;
    letter-spacing: 7px;
  }
</style>
</head>
<body>
  <section class="card" aria-label="Leaf Forge business card">
    <svg class="band" viewBox="0 0 1040 600" aria-hidden="true">
      <path d="M0 488 H790 C880 488 900 455 925 408 H1040 V600 H0 Z" fill="var(--leaf)"/>
    </svg>

    <h1 class="brand-name">Leaf Forge</h1>
    <p class="slogan">shaping every garden bright</p>

    <div class="person">
      <p class="person-name">Youssef Nabil Darwish</p>
      <p class="person-title">Founder &amp; CEO</p>
    </div>

    <ul class="contacts">
      <li>
        <svg viewBox="0 0 26 26" aria-hidden="true"><rect width="26" height="26" rx="4" fill="var(--leaf)"/><rect x="8" y="5" width="10" height="16" rx="1.5" fill="none" stroke="#fff" stroke-width="2"/><circle cx="13" cy="18" r="1" fill="#fff"/></svg>
        <span>01287719462</span>
      </li>
      <li>
        <svg viewBox="0 0 26 26" aria-hidden="true"><rect width="26" height="26" rx="4" fill="var(--leaf)"/><path d="M9 6 C6 9 7 15 11 19 C14 21 17 21 19 19 L17 16 L15 17 C13 16 11 13 11 11 L12 9 Z" fill="#fff"/></svg>
        <span>(02) 25948017</span>
      </li>
      <li>
        <svg viewBox="0 0 26 26" aria-hidden="true"><rect width="26" height="26" rx="4" fill="var(--leaf)"/><path d="M13 4 C9 4 7 7 7 10 C7 14 13 21 13 21 C13 21 19 14 19 10 C19 7 17 4 13 4 Z" fill="#fff"/><circle cx="13" cy="10" r="2.4" fill="var(--leaf)"/></svg>
        <span>27 El-Masry Street Ground Floor,<br>Ste.1 El-Marg,Cairo,Egypt</span>
      </li>
      <li>
        <svg viewBox="0 0 26 26" aria-hidden="true"><rect x="2" y="6" width="22" height="15" fill="none" stroke="var(--leaf)" stroke-width="2.4"/><path d="M2 6 L13 15 L24 6" fill="none" stroke="var(--leaf)" stroke-width="2.4"/></svg>
        <span>youssef_nabil@leafforge.example</span>
      </li>
    </ul>

    <p class="website">www.leafforge.example</p>
  </section>
</body>
</html>
```